New, modern business card for growing audiology practice

We need a new business card for our audiology practice. Our logo and website have recently changed (more modern) and we want our business cards to reflect this change.
We conduct hearing tests, perform earwax removals, and fit & dispense hearing aids to our patients. We are a family owned practice in which the owner is the one who works directly with the patient. I have attached logos in various formats to use, as well as two ideas I found on this website; as well as a scanned copy of our current logo. Good luck!

Industry/Entity Type

Business

Contact Information for Business Card

Company name: Birchmont Hearing Center
Provider name: Peter Lowsby, Au.D. F/NSO
Phone number: (555) 318-6042
Address: 287 W. Hollister Rd. Alderbrook, OH 40000
email: birchmonthearing@quillpost.net
website: birchmonthearing.net

Colors
000000
aaaaaa
dbdbdb
cacaca
9bcb3c
afd23c
cadf82
b1b1b1

Requirements
Must have
• My card must include information in the "details" section. In the attached images, I found a few that I liked and I would like to model after - "steady strivin'" and "Sound Lab Clinic".
• Must be horizontal.
• Must include logos provided. I uploaded them in various file formats and various ways.
• Must match logo font, if possible, if not, please get as close as you can.
Nice to have
• I really like the idea of having a color on one side with just the logo and company name and the contact information and provider name on the other side. I also really like the idea of having the main color dominating on the logo/company side with accent of that same color on the contact side of the card.
Should not have
• Must not be vertical.

```html
<!DOCTYPE html>
<html lang="en">
<head>
<meta charset="utf-8">
<title>Birchmont Hearing Center — Business Card</title>
<link rel="stylesheet" href="https://fonts.googleapis.com/css2?family=Cabin:wght@400;600&family=PT+Sans:wght@400;700&display=swap">
<style>
  :root {
    --ink: #000000;
    --paper: #ffffff;
    --backdrop: #e4e4e4;
    --green: #7aab2e;
    --grey-text: #444444;
    --rule: #555555;
    --card-shadow: rgba(0, 0, 0, 0.18);
  }
  * { box-sizing: border-box; margin: 0; padding: 0; }
  html, body {
    width: 1200px;
    height: 900px;
    overflow: hidden;
  }
  body {
    background: var(--backdrop);
    display: flex;
    flex-direction: column;
    align-items: center;
    justify-content: center;
    gap: 44px;
    font-family: "PT Sans", Arial, sans-serif;
  }
  .card {
    width: 630px;
    height: 360px;
    position: relative;
    box-shadow: 0 10px 28px var(--card-shadow);
    overflow: hidden;
  }

  /* Front side */
  .card--front {
    background:
      radial-gradient(ellipse 55% 85% at 66% 30%, #2c2c2c 0%, #141414 55%, var(--ink) 100%);
  }
  .card--front .brand-name {
    position: absolute;
    left: 40px;
    right: 0;
    top: 160px;
    text-align: center;
    font-family: "Cabin", "Gill Sans", sans-serif;
    font-weight: 400;
    font-size: 27px;
    letter-spacing: 0.5px;
    color: var(--paper);
  }

  /* Back side */
  .card--back {
    background: var(--paper);
    display: flex;
    align-items: center;
  }
  .brand-block {
    width: 340px;
    display: flex;
    flex-direction: column;
    align-items: center;
    gap: 26px;
    padding-top: 22px;
  }
  .brand-dot {
    width: 58px;
    height: 58px;
    border-radius: 50%;
    background: var(--green);
  }
  .brand-block .brand-name {
    font-family: "Cabin", "Gill Sans", sans-serif;
    font-weight: 400;
    font-size: 21px;
    letter-spacing: 0.3px;
    color: var(--ink);
  }
  .divider {
    width: 1px;
    height: 168px;
    background: var(--rule);
    margin-top: -30px;
  }
  .contact {
    padding-left: 18px;
    margin-top: -30px;
    color: var(--grey-text);
    font-size: 13.5px;
    line-height: 1.35;
  }
  .provider-name {
    font-weight: 700;
    font-size: 17px;
    color: var(--green);
    letter-spacing: 0.4px;
  }
  .provider-title {
    font-size: 13px;
    margin-bottom: 6px;
  }
  .contact-list { list-style: none; }
  .contact-list li {
    display: flex;
    align-items: flex-start;
    gap: 8px;
    margin-bottom: 3px;
  }
  .contact-list svg {
    flex: none;
    width: 11px;
    height: 11px;
    margin-top: 3px;
    fill: var(--green);
  }
</style>
</head>
<body>

  <section class="card card--front" aria-label="Card front">
    <p class="brand-name">BIRCHMONT HEARING CENTER</p>
  </section>

  <section class="card card--back" aria-label="Card back">
    <div class="brand-block">
      <span class="brand-dot"></span>
      <p class="brand-name">BIRCHMONT HEARING CENTER</p>
    </div>
    <span class="divider"></span>
    <div class="contact">
      <p class="provider-name">PETER LOWSBY,</p>
      <p class="provider-title">AU.D. F/NSO</p>
      <ul class="contact-list">
        <li>
          <svg viewBox="0 0 12 12" aria-hidden="true"><path d="M6 0a4 4 0 0 0-4 4c0 3 4 8 4 8s4-5 4-8a4 4 0 0 0-4-4zm0 5.6A1.6 1.6 0 1 1 6 2.4a1.6 1.6 0 0 1 0 3.2z"/></svg>
          <span>287 W. Hollister<br>Rd. Alderbrook, OH 40000</span>
        </li>
        <li>
          <svg viewBox="0 0 12 12" aria-hidden="true"><path d="M2.4 0.6 4.2 2.6 3.3 4.1c.7 1.6 2.9 3.8 4.6 4.6l1.5-.9 2 1.8-1.1 1.9C6 11.4.6 6 .5 1.7z"/></svg>
          <span>(555) 318-6042</span>
        </li>
        <li>
          <svg viewBox="0 0 12 12" aria-hidden="true"><path d="M0 2h12v1L6 7 0 3zM0 4.3l6 4 6-4V10H0z"/></svg>
          <span>birchmonthearing@quillpost.net</span>
        </li>
        <li>
          <svg viewBox="0 0 12 12" aria-hidden="true"><circle cx="6" cy="6" r="6"/></svg>
          <span>www.birchmonthearing.net</span>
        </li>
      </ul>
    </div>
  </section>

</body>
</html>
```